Artwork-Design (Cover) für Musikalbum
Zielgruppe
Wir sind eine Tonträgerfirma und bewegen uns im Low-Budget-Segment.
Aufgabenstellung
Artwork-Design (Cover) für ein Musikalbum : 'Ein langer Abend unter hellen Laternen'
Wir benötigen nicht das komplette Artwork, sondern ein Frontcover
(121 x 120 mm + 20 mm Beschnitt) wg. etwaiger Verschiebung der Positionierung.
Fertigstellung (Aufziehen des Inlays und Labels) erfolgt später bei uns im Hause.
Wir benötigen später eine offene psd-Datei mit allen Ebenen.
Wichtig: Schriften nicht gerastert ggfs. Schrift mitliefern.
Was wir uns vorstellen:
- Entsprechend der Musik Bild,
- Bildmaterial sollte bei pixelbrunnen, bildarena oder q-motiv ausgesucht werden, das Bildmaterial wird dann später auch von uns dort eingekauft.
- keine Künstlerfotos.
Wir freuen uns und sind sehr gespannt auf eure Vorschläge,
bei Fragen gerne mailen

```html
<!DOCTYPE html>
<html lang="de">
<head>
<meta charset="utf-8">
<title>Ein langer Abend unter hellen Laternen – Frontcover</title>
<link rel="stylesheet" href="https://fonts.googleapis.com/css2?family=Cormorant+Garamond:wght@500;600&display=swap">
<style>
  :root {
    --ochre: #b9873f;
    --amber: #d6a55a;
    --teal-light: #6f9a8c;
    --teal-dark: #1f3b3f;
    --rust: #8f3b24;
    --umber: #4a2418;
    --ink: #152628;
    --title: #ffffff;
  }
  html, body {
    margin: 0;
    padding: 0;
    width: 1200px;
    height: 1186px;
    overflow: hidden;
    background: var(--ink);
  }
  .cover {
    position: relative;
    width: 1200px;
    height: 1186px;
    overflow: hidden;
  }
  .cover-artwork {
    position: absolute;
    inset: 0;
    background:
      radial-gradient(ellipse 60% 38% at 28% 58%, rgba(168, 72, 44, 0.85), rgba(143, 59, 36, 0) 70%),
      radial-gradient(ellipse 55% 30% at 75% 30%, rgba(111, 154, 140, 0.7), rgba(111, 154, 140, 0) 70%),
      radial-gradient(ellipse 50% 30% at 15% 10%, rgba(214, 165, 90, 0.8), rgba(214, 165, 90, 0) 70%),
      radial-gradient(ellipse 45% 35% at 80% 85%, rgba(143, 59, 36, 0.6), rgba(143, 59, 36, 0) 70%),
      linear-gradient(180deg, var(--ochre) 0%, var(--teal-light) 28%, var(--rust) 50%, var(--umber) 68%, var(--teal-dark) 85%, var(--ink) 100%);
  }
  .album-title {
    position: absolute;
    left: 0;
    right: 0;
    margin: 0;
    text-align: center;
    color: var(--title);
    font-family: "Cormorant Garamond", Georgia, serif;
    font-weight: 500;
    text-transform: uppercase;
    text-shadow: 0 2px 6px rgba(20, 20, 20, 0.35);
  }
  .album-title .title-lead {
    position: absolute;
    left: 0;
    right: 0;
    top: 472px;
    font-size: 64px;
    line-height: 1;
    letter-spacing: 1px;
    font-weight: 600;
  }
  .album-title .title-main {
    position: absolute;
    left: 0;
    right: 0;
    top: 532px;
    font-size: 128px;
    line-height: 1;
    letter-spacing: 2px;
  }
</style>
</head>
<body>
  <main class="cover">
    <div class="cover-artwork" role="img" aria-label="Gemaltes Bild einer Violine mit Bogen vor einem Hintergrund aus Notenblättern in Ocker-, Türkis- und Rosttönen"></div>
    <h1 class="album-title">
      <span class="title-lead">Ein langer Abend unter</span>
      <span class="title-main">hellen Laternen</span>
    </h1>
  </main>
</body>
</html>
```